London Based Property Finding Company - have logo already

We find property for private purchasers and investors in London, UK.  We work for the BUYER, whereas estate agencies/real estate companies work for the seller. We offer a much more personalised service to UK and overseas purchasers.

We would like the following:

*A double sided business card

*A letterhead

We have attached two versions of the logo. Each logo style is set on two different coloured backgrounds. Please choose one of the two designs, whichever you prefer or feel more comfortable with, and produce one in black and one in white background.

This applies to both pieces of stationery.

THE BUSINESS CARD:

We would like the company name placed on its own on one side of the card and the contact details and what we do on the other.

e.g.

SIDE 1:

BRAMWELL PROPERTY FINDERS

SIDE 2:

Owen Bramwell

t: 0208 394 2860

m: +44(0)7932 418 507

e: info@bramwellpropertyfinders.co.uk

w: bramwellpropertyfinders.co.uk

London Property Finders and Search Agents

I will leave the layout up to you, but a minimalist layout is preferred. If you would like to put additional detial or design on the card then that is up to, but not specified.

It is optional to have the company name on side 2, but if you do use it, please make it smaller. than on the 1st side.

The design needs to be simple, professional and not too in your face.

If you are using the black background design on side 1 for the logo, then maybe a white backgounnd can be used on side 2 with a black typeface.

The type face for the contacts details should be sans serif standard typeface. Please experiment with the desciprtion.

-

THE LETTERHEAD;

You can experiment with the layout for the letterhead. e.g logo centre aligned on the top of the page with the contact details and address at the bottom of the page OR the logo, description running along a bar on the top of the page with the contact details and website address at the bottom. Please try and experiment with this, but the less 'busy', the better.

Here is info that needs to be on the letterhead.

Bramwell Property Finders

t: 0208 394 2860

m: +44(0)7932 418 507

(PLEASE NOTE; the below company info must be placed at the bottom of the page as a footer, in small text.)

Kestrand Holdings Ltd Trading as Bramwell Property Finders, a company registered in England & Wales, No.7351926 , Registered office is 41 Hollinmoor Court, Hollinmoor Road, London, SW9 3PL, t: 0208 394 2860, m: +44(0)7932 418 507, e: info@bramwellpropertyfinders.co.uk

Best of luck!

Thank you

Dear Designer,

I have now attached the supporting files to this brief.

Thanks,

Owen Bramwell
Bramwell Property Finders

```html
<!DOCTYPE html>
<html lang="en">
<head>
<meta charset="utf-8">
<title>Bramwell Property Finders — Letterhead Options</title>
<link rel="stylesheet" href="https://fonts.googleapis.com/css2?family=Arimo:wght@400;700&display=swap">
<style>
  :root {
    --board: #ffffff;
    --paper: #ffffff;
    --ink: #111111;
    --bar: #0c0c0c;
    --light: #ffffff;
    --accent: #2aa8e0;
    --shadow: rgba(0, 0, 0, 0.45);
  }
  * { margin: 0; padding: 0; box-sizing: border-box; }
  html, body { width: 1200px; height: 1004px; overflow: hidden; background: var(--board); }
  body { position: relative; font-family: "Arimo", Arial, sans-serif; color: var(--ink); }

  .option-label {
    position: absolute; top: 154px; font-size: 38px; font-weight: 400; line-height: 1;
    width: 40px; text-align: center;
  }
  .option-label--one { left: 263px; }
  .option-label--two { left: 848px; }

  .letterhead {
    position: absolute; background: var(--paper);
    box-shadow: 2px 3px 6px var(--shadow);
  }
  .letterhead--one { left: 75px; top: 218px; width: 505px; height: 657px; }
  .letterhead--two { left: 635px; top: 213px; width: 508px; height: 662px; }

  .sidebar {
    position: absolute; left: 0; top: 0; bottom: 0; background: var(--bar);
  }
  .letterhead--one .sidebar { width: 140px; }
  .letterhead--two .sidebar { width: 137px; }

  .brand {
    position: absolute; top: 36px; color: var(--light); font-weight: 700;
    text-align: right; line-height: 1;
  }
  .letterhead--one .brand { left: 22px; }
  .letterhead--two .brand { left: 20px; }
  .brand__name { display: block; font-size: 15.5px; letter-spacing: 0.6px; }
  .brand__tag { display: block; font-size: 7px; letter-spacing: 0.4px; margin-top: 3px; }

  .contact {
    position: absolute; list-style: none; font-size: 7px; font-weight: 700;
    line-height: 16.7px; color: var(--light);
  }
  .contact__item--accent { color: var(--accent); }
  .letterhead--one .contact { right: 10px; top: 582px; text-align: right; }
  .letterhead--two .contact { left: 14px; top: 586px; text-align: left; }

  .legal {
    position: absolute; font-size: 6px; line-height: 8.5px; text-align: center; color: var(--ink);
  }
  .letterhead--one .legal { left: 140px; right: 0; top: 622px; }
  .letterhead--two .legal { left: 137px; right: 0; top: 624px; }
</style>
</head>
<body>
  <div class="option-label option-label--one">1</div>
  <div class="option-label option-label--two">2</div>

  <section class="letterhead letterhead--one">
    <aside class="sidebar">
      <div class="brand">
        <span class="brand__name">BRAMWELL</span>
        <span class="brand__tag">PROPERTY FINDERS</span>
      </div>
      <ul class="contact">
        <li class="contact__item">0208 394 2860</li>
        <li class="contact__item contact__item--accent">+44(0)7932 418 507</li>
        <li class="contact__item">info@bramwellpropertyfinders.co.uk</li>
        <li class="contact__item contact__item--accent">bramwellpropertyfinders.co.uk</li>
      </ul>
    </aside>
    <footer class="legal">
      Kestrand Holdings Ltd Trading as Bramwell Property Finders, a company registered in England &amp; Wales, No.7351926.<br>
      Registered office is 41 Hollinmoor Court, Hollinmoor Road, London, SW9 3PL.<br>
      t: 0208 394 2860, m: +44(0)7932 418 507, e: info@bramwellpropertyfinders.co.uk
    </footer>
  </section>

  <section class="letterhead letterhead--two">
    <aside class="sidebar">
      <div class="brand">
        <span class="brand__name">BRAMWELL</span>
        <span class="brand__tag">PROPERTY FINDERS</span>
      </div>
      <ul class="contact">
        <li class="contact__item">0208 394 2860</li>
        <li class="contact__item contact__item--accent">+44(0)7932 418 507</li>
        <li class="contact__item">info@bramwellpropertyfinders.co.uk</li>
        <li class="contact__item contact__item--accent">bramwellpropertyfinders.co.uk</li>
      </ul>
    </aside>
    <footer class="legal">
      Kestrand Holdings Ltd Trading as Bramwell Property Finders, a company registered in England &amp; Wales, No.7351926.<br>
      Registered office is 41 Hollinmoor Court, Hollinmoor Road, London, SW9 3PL.<br>
      t: 0208 394 2860, m: +44(0)7932 418 507, e: info@bramwellpropertyfinders.co.uk
    </footer>
  </section>
</body>
</html>
```